Maplerise Trading Inc. needs an innovative idea for letterhead and visiting cards.

Maplerise Trading Inc. is a Canadian brand since 2007. It is a renown dealer of kids and office furniture locally. Moreover, exporting electric fixtures e.g. switches, LED's, down-lights etc. to Middle East and Africa. We have initiated a number of steps including re-branding, to boost our export in 2020. We have successfully designed our new logo a few months ago through 'Artfolio' and now we are looking for an innovative idea for a letterhead.
Some key points:
• Red, black and white are the three colors used in all our packaging and furniture. (grey is optional)
• Shouldn’t be too wide.
• Use of watermark is preferable.
• You can visit our North American site at www.mapleriseinc.com. Export website of the company will be launched soon. www.mapleriseinc.ca
• Same letterhead will be used locally and internationally.
• Our new logo and sample packaging is attached.

```html
<!DOCTYPE html>
<html lang="en">
<head>
<meta charset="utf-8">
<title>Maplerise Trading – Letterhead &amp; Business Cards</title>
<link rel="stylesheet" href="https://fonts.googleapis.com/css2?family=Roboto:wght@400;500;700&family=Tinos&display=swap">
<style>
  :root {
    --bg: #e3e4e5;
    --paper: #f5f5f5;
    --card: #f7f7f7;
    --red: #9b0e14;
    --ink: #4a4a4a;
    --dark: #262626;
    --watermark: #efe3e4;
  }
  * { margin: 0; padding: 0; box-sizing: border-box; }
  html, body { width: 1200px; height: 1200px; overflow: hidden; background: var(--bg); }
  body { position: relative; font-family: "Roboto", sans-serif; color: var(--ink); }

  .sheet { position: absolute; background: var(--paper); }
  .letterhead { left: 73px; top: 148px; width: 721px; height: 935px; }

  .brand { position: absolute; display: flex; align-items: center; gap: 8px; }
  .brand-mark { border: 3px solid var(--red); border-radius: 6px; flex: none; }
  .brand-name { font-family: "Roboto", sans-serif; font-weight: 500; color: var(--red); line-height: 1.05; }

  .letterhead .brand { left: 58px; top: 46px; }
  .letterhead .brand-mark { width: 56px; height: 56px; }
  .letterhead .brand-name { font-size: 27px; }

  .contact { position: absolute; font-size: 11px; line-height: 13px; color: var(--ink); font-style: normal; }
  .contact .rule-red, .contact .rule-grey { position: absolute; left: -17px; width: 1.5px; }
  .contact .rule-red { background: var(--red); }
  .contact .rule-grey { background: var(--ink); }
  .contact .address { margin-bottom: 4px; }
  .contact .row { display: flex; align-items: center; gap: 4px; }
  .contact svg { flex: none; }

  .letterhead .contact { left: 533px; top: 48px; }
  .letterhead .rule-red { top: 0; height: 23px; }
  .letterhead .rule-grey { top: 30px; height: 37px; }

  .watermark { position: absolute; left: 244px; top: 354px; width: 233px; height: 234px;
    border: 10px solid var(--watermark); border-radius: 30px; }

  .band { position: absolute; left: 0; right: 0; bottom: 0; display: flex; gap: 2px; }
  .band .dark { background: var(--dark); }
  .band .red { background: var(--red); flex: 1; }
  .letterhead .band { height: 13px; }
  .letterhead .band .dark { width: 360px; }

  .card { width: 297px; height: 170px; }
  .card-back { left: 838px; top: 339px; overflow: hidden; }
  .card-back .pattern { position: absolute; inset: 0;
    background: linear-gradient(115deg, #6a6a6a 0%, #2b2b2b 35%, #161616 70%, #0d0d0d 100%); }
  .tagline { position: absolute; right: 14px; top: 117px; font-family: "Tinos", serif;
    font-size: 11.5px; color: #f1f1f1; letter-spacing: 0.2px; }

  .card-front { left: 838px; top: 565px; background: var(--card); }
  .card-front .brand { left: 20px; top: 68px; gap: 5px; }
  .card-front .brand-mark { width: 30px; height: 30px; border-width: 2px; border-radius: 4px; }
  .card-front .brand-name { font-size: 13px; }
  .card-front .contact { left: 161px; top: 44px; font-size: 8px; line-height: 10px; }
  .card-front .rule-red { left: -13px; top: 0; height: 22px; width: 1px; }
  .card-front .rule-grey { left: -13px; top: 27px; height: 55px; width: 1px; }
  .person { margin-bottom: 8px; }
  .person .name { font-size: 10px; font-weight: 700; color: var(--red); line-height: 12px; }
  .person .role { font-size: 8px; }
  .card-front .band { height: 7px; }
  .card-front .band .dark { width: 147px; }
</style>
</head>
<body>

<section class="sheet letterhead">
  <div class="brand">
    <span class="brand-mark"></span>
    <span class="brand-name">Maplerise<br>Trading</span>
  </div>

  <address class="contact">
    <span class="rule-red"></span><span class="rule-grey"></span>
    <div class="address">48 Birchwood Ave, Unit 205<br>Markham, ON L3R 2K9</div>
    <div class="row"><svg width="9" height="9" viewBox="0 0 10 10"><path d="M2 0.5l2 2-1 1.2c.6 1.3 1.8 2.5 3.1 3.1L7.3 5.8l2 2L8 9.5C4.2 9.3.7 5.8.5 2z" fill="#9b0e14"/></svg>+1 (888) 555-0142</div>
    <div class="row"><svg width="9" height="9" viewBox="0 0 10 10"><rect x="0.7" y="2" width="8.6" height="6" fill="none" stroke="#9b0e14" stroke-width="1.2"/><path d="M0.7 2L5 5.5 9.3 2" fill="none" stroke="#9b0e14" stroke-width="1.1"/></svg>info@mapleriseinc.com</div>
    <div class="row"><svg width="9" height="9" viewBox="0 0 10 10"><g fill="none" stroke="#9b0e14" stroke-width="0.9"><circle cx="5" cy="5" r="4.2"/><ellipse cx="5" cy="5" rx="1.8" ry="4.2"/><path d="M0.8 5h8.4M1.5 3h7M1.5 7h7"/></g></svg>www.mapleriseinc.com</div>
  </address>

  <div class="watermark" aria-hidden="true"></div>

  <div class="band"><span class="dark"></span><span class="red"></span></div>
</section>

<section class="sheet card card-back">
  <div class="pattern" role="img" aria-label="Repeating grid of brand emblems fading from silver to black"></div>
  <p class="tagline">Quality Built For Every Space</p>
</section>

<section class="sheet card card-front">
  <div class="brand">
    <span class="brand-mark"></span>
    <span class="brand-name">Maplerise<br>Trading</span>
  </div>

  <address class="contact">
    <span class="rule-red"></span><span class="rule-grey"></span>
    <div class="person"><div class="name">Daniel Carter</div><div class="role">Founder</div></div>
    <div class="address">48 Birchwood Ave, Unit 205<br>Markham, ON L3R 2K9</div>
    <div class="row"><svg width="7" height="7" viewBox="0 0 10 10"><path d="M2 0.5l2 2-1 1.2c.6 1.3 1.8 2.5 3.1 3.1L7.3 5.8l2 2L8 9.5C4.2 9.3.7 5.8.5 2z" fill="#9b0e14"/></svg>+1 (888) 555-0142</div>
    <div class="row"><svg width="7" height="7" viewBox="0 0 10 10"><rect x="0.7" y="2" width="8.6" height="6" fill="none" stroke="#9b0e14" stroke-width="1.2"/><path d="M0.7 2L5 5.5 9.3 2" fill="none" stroke="#9b0e14" stroke-width="1.1"/></svg>info@mapleriseinc.com</div>
    <div class="row"><svg width="7" height="7" viewBox="0 0 10 10"><g fill="none" stroke="#9b0e14" stroke-width="0.9"><circle cx="5" cy="5" r="4.2"/><ellipse cx="5" cy="5" rx="1.8" ry="4.2"/><path d="M0.8 5h8.4M1.5 3h7M1.5 7h7"/></g></svg>www.mapleriseinc.com</div>
  </address>

  <div class="band"><span class="dark"></span><span class="red"></span></div>
</section>

</body>
</html>
```